Brindle Paw & Pet Haulage

We need a new business card for a new business. We transport animals mainly dogs specialising in greyhounds travelling locally and interstate in air conditioned comfort. The design should incorporate the australian flag

Reason: just want to get the right design

Industry/Entity Type

Business

```html
<!DOCTYPE html>
<html lang="en">
<head>
<meta charset="utf-8">
<title>Brindle Paw &amp; Pet Haulage – Business Card</title>
<link href="https://fonts.googleapis.com/css2?family=Oswald:wght@600;700&family=Open+Sans:wght@400;600&display=swap" rel="stylesheet">
<style>
  :root {
    --navy: #0a2473;
    --red: #e3123f;
    --white: #ffffff;
    --backdrop: #e9e6e1;
    --art-warm: #c9976a;
    --art-orange: #f29a2e;
    --art-cream: #f3eed6;
  }
  html, body {
    margin: 0;
    padding: 0;
    width: 1200px;
    height: 1000px;
    overflow: hidden;
    background: var(--backdrop);
  }
  .business-card {
    position: absolute;
    left: 100px;
    top: 210px;
    width: 1000px;
    height: 580px;
    border-radius: 44px;
    overflow: hidden;
    box-shadow: 0 14px 40px rgba(0,0,0,0.18);
    background: var(--white);
  }
  .card-bands {
    position: absolute;
    inset: 0;
  }
  .mascot-art {
    position: absolute;
    top: 22px;
    left: 290px;
    width: 420px;
    height: 128px;
    border-radius: 22px;
    background: linear-gradient(90deg, var(--art-warm) 0%, var(--art-orange) 28%, var(--navy) 45%, var(--navy) 70%, var(--art-cream) 100%);
  }
  .brand-name {
    position: absolute;
    top: 148px;
    left: 0;
    width: 100%;
    text-align: center;
    margin: 0;
    font-family: "Oswald", sans-serif;
    font-weight: 700;
    font-size: 62px;
    line-height: 80px;
    letter-spacing: 0.5px;
    color: var(--navy);
    text-transform: uppercase;
  }
  .holder-name {
    position: absolute;
    top: 300px;
    left: 0;
    width: 100%;
    text-align: center;
    margin: 0;
    font-family: "Oswald", sans-serif;
    font-weight: 600;
    font-size: 48px;
    color: var(--white);
  }
  .contact-list {
    position: absolute;
    top: 405px;
    left: 0;
    width: 100%;
    margin: 0;
    padding: 0;
    list-style: none;
    text-align: center;
    font-family: "Open Sans", sans-serif;
    font-size: 27px;
    line-height: 40px;
    color: var(--white);
  }
  .contact-icon {
    width: 20px;
    height: 20px;
    vertical-align: -2px;
    margin-right: 6px;
  }
</style>
</head>
<body>
  <div class="business-card">
    <svg class="card-bands" width="1000" height="580" viewBox="0 0 1000 580" aria-hidden="true">
      <polygon points="0,232 1000,300 1000,580 0,580" fill="var(--red)"/>
      <polygon points="0,244 1000,312 1000,580 0,580" fill="var(--navy)"/>
    </svg>

    <div class="mascot-art" role="img" aria-label="Cartoon dog and cat riding in a car painted with the Australian flag, with a dust cloud behind"></div>

    <h1 class="brand-name">Brindle Paw &amp; Pet Haulage</h1>
    <p class="holder-name">Liam Harcourt</p>

    <ul class="contact-list">
      <li>
        <svg class="contact-icon" viewBox="0 0 20 20" aria-hidden="true">
          <rect x="5" y="1" width="10" height="18" rx="2" fill="none" stroke="var(--white)" stroke-width="2"/>
          <line x1="8" y1="15.5" x2="12" y2="15.5" stroke="var(--white)" stroke-width="1.6"/>
        </svg>0412 555 308
      </li>
      <li>ABN 51824067319</li>
      <li>
        <svg class="contact-icon" viewBox="0 0 20 20" aria-hidden="true">
          <g fill="none" stroke="var(--white)" stroke-width="1.5">
            <circle cx="10" cy="10" r="8.5"/>
            <ellipse cx="10" cy="10" rx="3.8" ry="8.5"/>
            <line x1="1.5" y1="10" x2="18.5" y2="10"/>
            <line x1="3" y1="5.5" x2="17" y2="5.5"/>
            <line x1="3" y1="14.5" x2="17" y2="14.5"/>
          </g>
        </svg>www.brindlepawhaulage.com
      </li>
    </ul>
  </div>
</body>
</html>
```